DL size flyer design for renovations and extensions construction company

We are looking for a flyer design for a construction company specialising in renovations, extensions, and minor building works. The aim is for anyone needing any home construction works to pick up the phone and call us. The flyers will be delivered primarily to letterboxes of homes. We want the flyers to stick out from all the other things people get in the mail by any means possible.

Target Market(s)

The audience we target is residential home owners and are looking to deliver these letters to home letterboxes.

Industry/Entity Type

Residential Construction

Font styles to use
Sans Serif

Colors
000000
ffffff

Requirements
Must have
• 1 - Places for 4 photos with descriptions reading: (1) Bathroom Renovations (4) Kitchen Renovations (3) Home Extensions (4) Outdoor works and landscaping. This may be on the reverse side of the DL flyer.
• 2 - Fonts to be used are (1) Brandon Grotesque (All caps) for main heading, (2) Montserrat SemiBold (All caps) for Headings, (3) Lato for text.
• 3 - Copy of the finished document in PDF and indesign formats.
• 4 - Placeholders for copy (look at the pelvaridge.com website for now)
Nice to have
• A modern looking design.
Should not have
• Not all photos attached are necessarily required. Up to you to use your creativity to decide on the best combination.

```html
<!DOCTYPE html>
<html lang="en">
<head>
<meta charset="utf-8">
<title>Pelvaridge – DL Flyer</title>
<link href="https://fonts.googleapis.com/css2?family=Lato:wght@400;700&family=Montserrat:wght@500;600;700;800&display=swap" rel="stylesheet">
<style>
  :root{
    --canvas:#d6d6d6;
    --black:#000000;
    --white:#ffffff;
    --green:#1f9a5e;
    --rule:#5a5a5a;
  }
  *{box-sizing:border-box;margin:0;padding:0}
  html,body{width:1200px;height:1200px;overflow:hidden;background:var(--canvas)}
  body{position:relative;font-family:"Lato",sans-serif;color:var(--white)}
  .panel{position:absolute;top:135px;width:439px;height:930px;background:var(--black);overflow:hidden}
  .front{left:131px}
  .back{left:632px}
  .abs{position:absolute}
  .center{left:0;right:0;text-align:center}

  /* front */
  .brand-bar{top:0;left:0;width:100%;height:77px;background:var(--white);display:flex;align-items:center;justify-content:center}
  .brand-name{font-family:"Montserrat",sans-serif;font-weight:800;font-size:40px;letter-spacing:1px;color:var(--black)}
  .tagline{top:89px;font-family:"Montserrat",sans-serif;font-weight:600;font-size:14px;letter-spacing:1px}
  .question{top:112px;font-family:"Montserrat",sans-serif;font-weight:600;font-size:19px;letter-spacing:.5px}
  .big{font-family:"Montserrat",sans-serif;font-weight:800;color:var(--green);letter-spacing:4px;line-height:1}
  .big-1{top:142px;font-size:66px}
  .big-or{top:220px;font-size:34px;letter-spacing:2px}
  .big-2{top:258px;font-size:66px}
  .hero-photo{top:348px;left:0;width:100%;height:282px;background:linear-gradient(90deg,#b9b2a4 0%,#8f8a7c 35%,#8aa07a 55%,#c9ccd0 75%,#e9eaec 100%)}
  .excellence{top:647px;font-family:"Montserrat",sans-serif;font-weight:700;font-size:20px;letter-spacing:.5px}
  .about{top:684px;left:40px;right:40px;text-align:center;font-size:12.3px;line-height:15.1px}
  .rule{height:1px;background:var(--rule)}
  .rule-a{top:824px;left:44px;right:44px}
  .rule-b{top:877px;left:44px;right:44px}
  .phone-big{display:flex;align-items:center;justify-content:center;gap:8px;font-family:"Montserrat",sans-serif;font-weight:600;font-size:38px;letter-spacing:.5px}
  .front .phone-big{top:830px}
  .site{display:flex;align-items:center;justify-content:center;gap:6px;font-family:"Montserrat",sans-serif;font-weight:600;font-size:12px;letter-spacing:.5px}
  .front .site{top:884px}

  /* back */
  .back .site{top:21px}
  .services-band{top:40px;left:0;width:100%;height:27px;background:var(--white);color:var(--black);text-align:center;font-family:"Montserrat",sans-serif;font-weight:700;font-size:18px;line-height:29px}
  .intro{top:76px;left:40px;right:40px;text-align:center;font-size:9px;line-height:11.3px}
  .divider-v{top:142px;left:218px;width:1px;height:590px;background:var(--rule)}
  .divider-h{top:457px;left:32px;right:44px;height:1px;background:var(--rule)}
  .diamond{width:9px;height:9px;border:1px solid var(--white);background:var(--black);transform:rotate(45deg)}
  .service{position:absolute;width:178px}
  .service .photo{width:178px;height:120px;border:4px solid var(--white)}
  .service h3{margin-top:12px;font-family:"Montserrat",sans-serif;font-weight:600;font-size:11.2px;line-height:15px;text-transform:uppercase;white-space:nowrap}
  .service p{margin-top:5px;font-size:9px;line-height:11.3px}
  .service p + p{margin-top:11px}
  .s-bath{left:32px;top:142px}
  .s-kitchen{left:230px;top:142px}
  .s-struct{left:32px;top:466px}
  .s-outdoor{left:230px;top:466px}
  .ph-bath{background:linear-gradient(135deg,#e9e9ea,#b8b6b3)}
  .ph-kitchen{background:linear-gradient(135deg,#d9dfd9,#c8b49a)}
  .ph-struct{background:linear-gradient(135deg,#e2ddd7,#9c6b45)}
  .ph-outdoor{background:linear-gradient(135deg,#2a2520,#5f6e4a)}
  .contact-area{top:745px;left:0;width:100%;height:185px;background:linear-gradient(180deg,#e9e9e9,#f7f5f3)}
  .back .phone-big{top:751px;color:var(--black)}
  .contact-row{top:796px;left:0;width:100%;height:12px;display:flex;justify-content:center;gap:20px;background:var(--white);color:var(--black);font-family:"Montserrat",sans-serif;font-weight:600;font-size:9px;line-height:12px}
  .contact-row span{display:flex;align-items:center;gap:5px}
  .bath-photo{top:808px;left:0;width:100%;height:122px;background:linear-gradient(90deg,#f4f1ee 0%,#e9d5c4 45%,#f1e6dc 70%,#f6f3f0 100%)}
</style>
</head>
<body>

<section class="panel front">
  <header class="abs brand-bar"><span class="brand-name">PELVARIDGE</span></header>
  <p class="abs center tagline">BUILD.&nbsp; RENOVATE.&nbsp; EXTEND.</p>
  <p class="abs center question">LOOKING TO MAKE YOUR HOME</p>
  <p class="abs center big big-1">BIGGER</p>
  <p class="abs center big big-or">OR</p>
  <p class="abs center big big-2">BETTER?</p>
  <div class="abs hero-photo" role="img" aria-label="Before and after photo of a rundown rear house facade transformed by a modern glazed extension"></div>
  <h2 class="abs center excellence">COMMITTED TO EXCELLENCE</h2>
  <p class="abs about">Pelvaridge creates individual and exceptional home renovations and extensions built by experienced tradespeople using the best possible materials.<br>We form beautiful places to live based on the distinct vision and values of our clients, knowing that each project is unique. With a supervisor dedicated to your project there is no need to worry about coordinating tradespeople, finding the right person for the job, or cleaning up at the end of each day.</p>
  <div class="abs rule rule-a"></div>
  <p class="abs center phone-big">
    <svg width="26" height="26" viewBox="0 0 24 24" aria-hidden="true"><path fill="#fff" d="M6.6 10.8a15 15 0 0 0 6.6 6.6l2.2-2.2c.3-.3.7-.4 1-.2 1.1.4 2.3.6 3.6.6.6 0 1 .4 1 1V20c0 .6-.4 1-1 1C10.6 21 3 13.4 3 4c0-.6.4-1 1-1h3.5c.6 0 1 .4 1 1 0 1.3.2 2.5.6 3.6.1.3 0 .7-.2 1z"/></svg>
    0400 555 218
  </p>
  <div class="abs rule rule-b"></div>
  <p class="abs center site">
    <svg width="10" height="10" viewBox="0 0 10 10" aria-hidden="true"><circle cx="5" cy="5" r="4.2" fill="none" stroke="#fff" stroke-width="1"/><path d="M1 5h8M5 1v8" stroke="#fff" stroke-width=".8"/></svg>
    PELVARIDGE.COM
  </p>
</section>

<section class="panel back">
  <p class="abs center site">
    <svg width="10" height="10" viewBox="0 0 10 10" aria-hidden="true"><circle cx="5" cy="5" r="4.2" fill="none" stroke="#fff" stroke-width="1"/><path d="M1 5h8M5 1v8" stroke="#fff" stroke-width=".8"/></svg>
    PELVARIDGE.COM
  </p>
  <h2 class="abs services-band">SERVICES</h2>
  <p class="abs intro">Our building Works Span as far as your<br>ambitions. From custom kitchens and bathrooms, to<br>bespoke joinery for renovating your study, bedrooms, laundry and other living areas.<br>We can alter or extend the layout of your home, or create an escape from the daily<br>grind with landscape gardening and other outdoor works.</p>

  <div class="abs divider-v"></div>
  <div class="abs divider-h"></div>
  <div class="abs diamond" style="top:453px;left:214px"></div>
  <div class="abs diamond" style="top:716px;left:214px"></div>
  <div class="abs diamond" style="top:726px;left:214px"></div>

  <article class="service s-bath">
    <div class="photo ph-bath" role="img" aria-label="Bright modern bathroom with freestanding bath and glass shower"></div>
    <h3>Bathroom<br>Renovations</h3>
    <p>We create custom bathroom renovations of various shapes and sizes to suit a variety of family needs.</p>
    <p>When considering a bathroom design you will need to take into account a variety of factors including the size of the existing space and whether it can be enlarged, how many people in your family will use the bathroom, if your family size is likely to increase, where the bathroom is located in the home as well as many other considerations.</p>
  </article>

  <article class="service s-kitchen">
    <div class="photo ph-kitchen" role="img" aria-label="Family gathered around an island bench in a white open-plan kitchen"></div>
    <h3>Kitchen<br>Renovations</h3>
    <p>Today's kitchens go further than places to just make a meal - they are the open-plan hub for the modern home.</p>
    <p>Each kitchen will need to work in with each family's unique needs. That's why it's important to work in with an expert designer and builder on your renovation project.</p>
  </article>

  <article class="service s-struct">
    <div class="photo ph-struct" role="img" aria-label="Open-plan extension with timber dining table and pendant lights"></div>
    <h3>Structural Alterations<br>+ Extensions</h3>
    <p>Structural alterations or extensions are an essential consideration when things simply wont fit or you want to make your home bigger or better.</p>
    <p>Pelvaridge are licenced builders experienced at delivering structural alterations or home extensions, and we are always guided by our qualified engineers.</p>
  </article>

  <article class="service s-outdoor">
    <div class="photo ph-outdoor" role="img" aria-label="Covered outdoor patio with lounge furniture lit at night"></div>
    <h3>Outdoor Works and<br>Landscaping</h3>
    <p>Home living spans across both internal and external environments and a complete home needs to consider integration into the surrounding land.</p>
    <p>Whether it be landscaping works, swimming pools or outdoor buildings - Pelvaridge can deliver all project designs both large scale and compact.</p>
  </article>

  <div class="abs contact-area"></div>
  <p class="abs center phone-big">
    <svg width="26" height="26" viewBox="0 0 24 24" aria-hidden="true"><path fill="#000" d="M6.6 10.8a15 15 0 0 0 6.6 6.6l2.2-2.2c.3-.3.7-.4 1-.2 1.1.4 2.3.6 3.6.6.6 0 1 .4 1 1V20c0 .6-.4 1-1 1C10.6 21 3 13.4 3 4c0-.6.4-1 1-1h3.5c.6 0 1 .4 1 1 0 1.3.2 2.5.6 3.6.1.3 0 .7-.2 1z"/></svg>
    0400 555 218
  </p>
  <div class="abs contact-row">
    <span><svg width="11" height="8" viewBox="0 0 11 8" aria-hidden="true"><rect x=".5" y=".5" width="10" height="7" fill="none" stroke="#000"/><path d="M.5.5l5 4 5-4" fill="none" stroke="#000"/></svg>INFO@PELVARIDGE.COM</span>
    <span><svg width="7" height="10" viewBox="0 0 7 10" aria-hidden="true"><path d="M3.5 0A3.5 3.5 0 0 0 0 3.5C0 6 3.5 10 3.5 10S7 6 7 3.5A3.5 3.5 0 0 0 3.5 0zm0 5a1.5 1.5 0 1 1 0-3 1.5 1.5 0 0 1 0 3z" fill="#000"/></svg>SERVING MOST AREAS OF SYDNEY, NSW.</span>
  </div>
  <div class="abs bath-photo" role="img" aria-label="Woman relaxing in a bubble bath with candles in a bright bathroom"></div>
</section>

</body>
</html>
```